Wirenexa

I'm looking to much improve our current website wirenexa.com
Updates

Low design quality

Target Market(s)

Commercial clients (Not-Residentials)

Industry/Entity Type

Office buildings and Industrial clients

Coding

Coded - Design and coding required

Number of Pages Required

5+ page

Requirements
Must have
• Very professional structured low voltage cabling projects for Wi-Fi, Audio/Video conference rooms, Access Control systems, CCTV.

```html
<!DOCTYPE html>
<html lang="en">
<head>
<meta charset="utf-8">
<title>Wirenexa — Commercial Low-Voltage Cabling</title>
<link href="https://fonts.googleapis.com/css2?family=Archivo:wght@500;600;700;800&family=Inter:wght@400;500;600&family=JetBrains+Mono:wght@400;500&display=swap" rel="stylesheet">
<style>
:root{--red:#d71920;--red-soft:#fbe9ea;--ink:#141414;--body:#55524e;--muted:#9a958f;--bg:#f5f3f0;--white:#fff;--line:#e5e1dc}
*{box-sizing:border-box;margin:0;padding:0}
html,body{width:1200px;height:4573px;overflow:hidden}
body{background:var(--bg);font-family:Inter,sans-serif;color:var(--ink);font-size:11px;line-height:1.5}
.wrap{width:784px;margin:0 auto;position:relative}
.mono{font-family:"JetBrains Mono",monospace;letter-spacing:.14em;text-transform:uppercase;font-size:8px;color:var(--muted)}
.eyebrow{font-family:"JetBrains Mono",monospace;font-size:8px;letter-spacing:.16em;text-transform:uppercase;color:var(--red);display:flex;align-items:center;gap:8px}
.eyebrow::before{content:"";width:18px;height:1px;background:var(--red)}
.center{text-align:center}.eyebrow.c{justify-content:center}
h1,h2,h3,h4{font-family:Archivo,sans-serif;letter-spacing:-.02em}
h2{font-size:30px;line-height:1.05;font-weight:700;margin-top:10px}
h4{font-size:13px;font-weight:700}
.red{color:var(--red)}
.btn{display:inline-flex;align-items:center;gap:8px;height:40px;padding:0 22px;font-size:11px;font-weight:600;border-radius:2px}
.btn-red{background:var(--red);color:#fff}
.btn-line{border:1px solid var(--line);background:#fff}
.ico{width:28px;height:28px;background:var(--red-soft);display:flex;align-items:center;justify-content:center;border-radius:3px}
.ico svg{width:13px;height:13px;stroke:var(--red);fill:none;stroke-width:1.6}
/* nav */
.nav{height:50px;background:var(--bg);border-bottom:1px solid var(--line)}
.nav .wrap{display:flex;align-items:center;height:50px}
.logo{font-family:Archivo,sans-serif;font-weight:800;font-size:14px;display:flex;align-items:center;gap:5px}
.logo i{width:10px;height:10px;background:var(--red);display:block}
.nav ul{list-style:none;display:flex;gap:28px;margin-left:92px;font-size:10px;color:var(--body)}
.nav .phone{margin-left:auto;font-size:10px;font-weight:600;display:flex;align-items:center;gap:6px}
.nav .btn{height:34px;padding:0 18px;font-size:10px;margin-left:18px}
/* hero */
.hero{height:580px;background:linear-gradient(90deg,var(--bg) 50%,#f7eceb);position:relative;overflow:hidden}
.hero .grid-bg{position:absolute;inset:0;background-image:linear-gradient(var(--line) 1px,transparent 1px),linear-gradient(90deg,var(--line) 1px,transparent 1px);background-size:28px 28px;opacity:.35}
.hero-in{position:relative;width:826px;margin:0 auto;padding-top:70px}
.hero h1{font-size:50px;line-height:.98;font-weight:800;margin-top:12px;width:400px}
.hero p.lead{font-size:12px;color:var(--body);width:370px;margin-top:22px;line-height:1.6}
.hero .ctas{display:flex;gap:10px;margin-top:24px}
.hero .facts{display:flex;margin-top:30px}
.hero .fact{padding-right:24px;margin-right:24px;border-right:1px solid var(--line)}
.hero .fact:last-child{border:0}
.hero .fact b{font-family:Archivo,sans-serif;font-size:16px;display:block}
.hero-photo{position:absolute;left:498px;top:105px;width:328px;height:365px;background:linear-gradient(160deg,#3a6e6a,#1d2b2c 45%,#6f6b2c 90%)}
.badge30{position:absolute;left:478px;top:405px;width:84px;height:84px;border-radius:50%;background:var(--red);color:#fff;text-align:center;padding-top:16px;box-shadow:0 6px 18px rgba(215,25,32,.3)}
.badge30 b{font-family:Archivo,sans-serif;font-size:26px;display:block;line-height:1}
.badge30 span{font-family:"JetBrains Mono",monospace;font-size:6px;letter-spacing:.1em}
/* trust */
.trust{height:42px;background:#fff;border-bottom:1px solid var(--line)}
.trust-in{width:826px;margin:0 auto;display:flex;align-items:center;height:42px;gap:22px;font-size:8px;color:var(--body)}
.trust-in .mono{font-size:7px;margin-right:8px}
.trust-in span.t{display:flex;align-items:center;gap:5px}
.trust-in span.t::before{content:"";width:8px;height:8px;border:1px solid var(--red);border-radius:50%}
/* services */
.services{height:868px;padding-top:80px}
.sub{color:var(--body);font-size:10.5px;margin-top:12px;width:460px}
.svc-grid{display:grid;grid-template-columns:repeat(4,1fr);margin-top:40px;border:1px solid var(--line);background:#fff}
.svc{height:198px;padding:24px 20px;border-right:1px solid var(--line);border-bottom:1px solid var(--line);position:relative}
.svc:nth-child(4n){border-right:0}.svc:nth-child(n+5){border-bottom:0}
.svc .n{position:absolute;right:16px;top:16px;font-family:"JetBrains Mono",monospace;font-size:7px;color:var(--muted)}
.svc h4{margin:18px 0 6px}
.svc p{font-size:8.5px;color:var(--body);line-height:1.55}
.svc .mono{position:absolute;left:20px;bottom:22px;font-size:6.5px}
.scope{margin-top:16px;background:#fff;border:1px solid var(--line);height:136px;display:flex;align-items:center;padding:0 28px}
.scope .intro{width:220px}
.scope .intro h4{margin:6px 0 4px}
.scope .intro p{font-size:8.5px;color:var(--body)}
.scope ul{list-style:none;display:grid;grid-template-columns:repeat(3,1fr);gap:22px 20px;flex:1}
.scope li{font-size:8.5px;font-weight:600;padding-left:18px;position:relative}
.scope li small{display:block;font-weight:400;color:var(--body);font-size:7.5px}
.tick{position:absolute;left:0;top:1px;width:11px;height:11px}
/* serve */
.serve{height:520px;background:#fff;padding-top:76px}
.serve h2{width:420px;margin:10px auto 0}
.serve-grid{display:grid;grid-template-columns:repeat(3,1fr);gap:16px;margin-top:38px}
.seg{height:258px;border:1px solid var(--line);padding:28px 24px;position:relative}
.seg.pop{border-color:var(--red);background:linear-gradient(180deg,#fbe6e7,#fff 55%)}
.seg .tag{position:absolute;top:-1px;left:50%;transform:translateX(-50%);background:var(--red);color:#fff;font-family:"JetBrains Mono",monospace;font-size:6px;letter-spacing:.12em;padding:3px 8px}
.seg h4{margin:18px 0 8px}
.seg p{font-size:8.5px;color:var(--body);line-height:1.6}
.seg ul{list-style:none;margin-top:22px;display:grid;gap:9px}
.seg li{font-size:8px;padding-left:18px;position:relative}
/* why */
.why{height:560px;padding-top:80px}
.why-row{display:flex;gap:48px}
.why-photo{width:368px;height:422px;background:linear-gradient(150deg,#1c2430,#3a4654 50%,#b07a2c);position:relative}
.why-photo span{position:absolute;left:12px;bottom:8px;color:#d7d2cb;font-size:6.5px}
.why-text{flex:1;padding-top:0}
.why-list{margin-top:22px}
.why-item{display:flex;gap:14px;padding:18px 0;border-top:1px solid var(--line)}
.why-item:first-child{border-top:0}
.why-item .ico{width:20px;height:20px;flex:none}
.why-item .ico svg{width:10px;height:10px}
.why-item b{font-size:10px;font-family:Archivo,sans-serif}
.why-item p{font-size:8.5px;color:var(--body);margin-top:4px}
/* stats */
.stats{height:220px;padding-top:20px}
.stat-row{display:grid;grid-template-columns:repeat(4,1fr);border:1px solid var(--line)}
.stat{height:150px;border-right:1px solid var(--line);text-align:center;padding-top:34px}
.stat:last-child{border:0}
.stat b{font-family:Archivo,sans-serif;font-size:36px;font-weight:700;display:block;line-height:1}
.stat i{display:block;width:4px;height:4px;background:var(--red);border-radius:50%;margin:12px auto 10px}
.stat .mono{font-size:7px}
/* process */
.process{height:364px;padding-top:24px}
.process h2{width:360px;margin:10px auto 0}
.steps{display:grid;grid-template-columns:repeat(4,1fr);margin-top:36px;border:1px solid var(--line);background:#fff}
.step{height:156px;padding:24px 20px;border-right:1px solid var(--line)}
.step:last-child{border:0}
.step .k{font-family:"JetBrains Mono",monospace;font-size:8px;color:var(--red);letter-spacing:.1em}
.step h4{margin:12px 0 6px;font-size:12px}
.step p{font-size:8.5px;color:var(--body)}
/* reviews */
.reviews{height:506px;background:#fff;padding-top:80px}
.reviews h2{width:340px;margin:10px auto 0}
.rev-grid{display:grid;grid-template-columns:repeat(3,1fr);gap:16px;margin-top:38px}
.rev{height:176px;border:1px solid var(--line);padding:22px 20px;position:relative}
.stars{color:var(--red);letter-spacing:2px;font-size:11px}
.rev p{font-size:9px;line-height:1.6;margin-top:10px}
.who{position:absolute;left:20px;bottom:20px;display:flex;gap:10px;align-items:center}
.who i{width:24px;height:24px;border-radius:50%;background:var(--red-soft);color:var(--red);font-style:normal;font-size:8px;display:flex;align-items:center;justify-content:center}
.who b{font-size:8.5px;display:block}
.who .mono{font-size:6.5px;letter-spacing:.06em}
.rated{text-align:center;margin-top:28px;font-size:7px}
/* contact */
.contact{height:586px;background:linear-gradient(180deg,#f7e5e4,var(--bg) 40%);padding-top:70px}
.contact-row{display:flex;gap:48px}
.contact-left{width:368px;padding-top:10px}
.contact-left h2{font-size:32px}
.contact-left .sub{width:330px}
.cinfo{margin-top:30px}
.crow{display:flex;gap:18px;padding:18px 0;border-top:1px solid var(--line);align-items:flex-start}
.crow:first-child{border-top:0}
.crow .mono{font-size:6.5px}
.crow b{font-size:10px;display:block}
.crow small{font-size:7.5px;color:var(--body)}
.form{flex:1;background:#fff;border:1px solid var(--line);padding:26px 24px;height:466px}
.form h4{font-size:15px;margin:6px 0 18px}
.frow{display:grid;grid-template-columns:1fr 1fr;gap:10px;margin-bottom:12px}
.field label{font-size:7px;font-weight:600;display:block;margin-bottom:5px}
.field .in{height:30px;border:1px solid var(--line);background:#fafaf8;font-size:8px;color:var(--muted);padding:0 10px;display:flex;align-items:center}
.field .in.sel{color:var(--ink);justify-content:space-between}
.field .in.ta{height:64px;align-items:flex-start;padding-top:8px}
.form .btn{width:100%;justify-content:center;margin-top:16px;height:36px}
.form .note{text-align:center;margin-top:14px;font-size:6.5px;letter-spacing:.04em;text-transform:none}
/* footer */
.footer{height:277px;background:#fff;padding-top:60px}
.fcols{display:grid;grid-template-columns:1.35fr 1fr 1fr 1fr;gap:24px}
.fcols p{font-size:8px;color:var(--body);margin-top:12px;width:200px}
.fcols .mono{font-size:6.5px}
.fcols ul{list-style:none;margin-top:12px;display:grid;gap:9px;font-size:8px;color:var(--body)}
.fbottom{display:flex;justify-content:space-between;margin-top:70px;padding-top:14px;border-top:1px solid var(--line)}
.fbottom .mono{font-size:6.5px;letter-spacing:.06em}
</style>
</head>
<body>
<svg width="0" height="0" style="position:absolute"><defs><symbol id="tk" viewBox="0 0 12 12"><path d="M2 6.3l2.6 2.5L10 3.3" fill="none" stroke="#d71920" stroke-width="1.6"/></symbol></defs></svg>

<header class="nav"><div class="wrap">
  <div class="logo"><i></i>Wirenexa</div>
  <ul><li>Services</li><li>Why Us</li><li>Process</li><li>Reviews</li><li>Contact</li></ul>
  <div class="phone"><svg width="10" height="10" viewBox="0 0 24 24" fill="none" stroke="#d71920" stroke-width="2"><path d="M5 3h4l2 5-3 2a12 12 0 0 0 6 6l2-3 5 2v4a2 2 0 0 1-2 2A18 18 0 0 1 3 5a2 2 0 0 1 2-2z"/></svg>(888) 555-0142</div>
  <span class="btn btn-red">Request a Quote</span>
</div></header>

<section class="hero">
  <div class="grid-bg"></div>
  <div class="hero-in">
    <div class="eyebrow">Commercial low-voltage · VA · DC · MD</div>
    <h1>The infrastructure your business <span class="red">runs on.</span></h1>
    <p class="lead">Structured cabling, surveillance, access control and connectivity — engineered, installed and certified for commercial and industrial facilities. Thirty years of doing it right the first time.</p>
    <div class="ctas"><span class="btn btn-red">Request a Quote →</span><span class="btn btn-line">☏ (888) 555-0142</span></div>
    <div class="facts">
      <div class="fact"><b>Est. 1995</b><span class="mono">30 years in business</span></div>
      <div class="fact"><b>Verilink Certified</b><span class="mono">LX-8000 testing</span></div>
      <div class="fact"><b>1-Hour</b><span class="mono">Quote response</span></div>
    </div>
    <div class="hero-photo" role="img" aria-label="Server rack with neatly dressed teal and yellow patch cables"></div>
    <div class="badge30"><b>30</b><span>YEARS INSTALLED<br>1995–2025</span></div>
  </div>
</section>

<div class="trust"><div class="trust-in">
  <span class="mono">Trusted by commercial &amp; industrial clients across the DMV</span>
  <span class="t">Licensed &amp; Insured</span><span class="t">24/7 Support</span><span class="t">CableGuild Best Practices</span><span class="t">Works With Your IT Team</span>
</div></div>

<section class="services"><div class="wrap">
  <div class="eyebrow">What we do</div>
  <h2>One contractor for every low-<br>voltage system in your building.</h2>
  <p class="sub">From the riser to the rack to the rooftop dish — we design, install, terminate and certify the systems that keep commercial operations connected and secure.</p>
  <div class="svc-grid">
    <div class="svc"><span class="n">01</span><div class="ico"><svg viewBox="0 0 24 24"><circle cx="12" cy="5" r="2"/><circle cx="5" cy="19" r="2"/><circle cx="19" cy="19" r="2"/><path d="M12 7v5M5 17l7-5 7 5"/></svg></div><h4>Structured Cabling</h4><p>CAT6 / CAT6A / CAT7 copper backbone and horizontal cabling, IDF/MDF buildouts and clean cable management.</p><span class="mono">Copper · voice &amp; data →</span></div>
    <div class="svc"><span class="n">02</span><div class="ico"><svg viewBox="0 0 24 24"><path d="M4 12h16M12 4v16"/></svg></div><h4>Fiber Optic</h4><p>Single-mode and multimode fiber installation, fusion splicing, termination and OTDR testing for high-bandwidth links.</p><span class="mono">SM · MM · splicing →</span></div>
    <div class="svc"><span class="n">03</span><div class="ico"><svg viewBox="0 0 24 24"><rect x="3" y="7" width="13" height="10" rx="1"/><path d="M16 11l5-3v8l-5-3"/></svg></div><h4>Video Surveillance</h4><p>IP camera systems, NVR/VMS, PoE infrastructure and remote monitoring designed to cover every blind spot.</p><span class="mono">IP CCTV · NVR →</span></div>
    <div class="svc"><span class="n">04</span><div class="ico"><svg viewBox="0 0 24 24"><circle cx="8" cy="15" r="4"/><path d="M11 12l8-8M16 7l2 2"/></svg></div><h4>Access Control</h4><p>Card, fob and mobile credential systems, electric strikes and maglocks, with integration into your existing directory.</p><span class="mono">Badge · mobile · maglock →</span></div>
    <div class="svc"><span class="n">05</span><div class="ico"><svg viewBox="0 0 24 24"><path d="M2 9a15 15 0 0 1 20 0M5 13a10 10 0 0 1 14 0M9 17a4 4 0 0 1 6 0"/></svg></div><h4>Wireless Access Points</h4><p>Predictive Wi-Fi design, heat-mapping and WAP installation for full-coverage, high-density commercial environments.</p><span class="mono">Wi-Fi 6/6E · heat-map →</span></div>
    <div class="svc"><span class="n">06</span><div class="ico"><svg viewBox="0 0 24 24"><rect x="3" y="6" width="18" height="12" rx="1"/><path d="M3 10h18"/></svg></div><h4>Point of Sale</h4><p>Dedicated cabling and network drops for POS terminals, kiosks and payment hardware across retail and hospitality.</p><span class="mono">Retail · hospitality →</span></div>
    <div class="svc"><span class="n">07</span><div class="ico"><svg viewBox="0 0 24 24"><path d="M5 19a10 10 0 0 1 0-14l14 14a10 10 0 0 1-14 0zM14 10l5-5"/></svg></div><h4>Skyvault Installation</h4><p>Professional mounting, weatherproofing and network integration for Skyvault — primary or failover connectivity anywhere.</p><span class="mono">Mount · failover →</span></div>
    <div class="svc"><span class="n">08</span><div class="ico"><svg viewBox="0 0 24 24"><rect x="3" y="4" width="18" height="12" rx="1"/><path d="M9 20h6M12 16v4"/></svg></div><h4>Conference Room Tech</h4><p>Displays, video conferencing, audio and control systems — fully cabled and commissioned meeting spaces.</p><span class="mono">VC · AV · control →</span></div>
  </div>
  <div class="scope">
    <div class="intro"><div class="eyebrow">Full scope</div><h4>Included on every project.</h4><p>We handle the whole job end-to-end — not just the cable pull.</p></div>
    <ul>
      <li><svg class="tick"><use href="#tk"/></svg>Cabling<small>Copper &amp; fiber pulls, terminations</small></li>
      <li><svg class="tick"><use href="#tk"/></svg>Wi-Fi<small>WAP design, heat-mapping &amp; setup</small></li>
      <li><svg class="tick"><use href="#tk"/></svg>IDF / MDF<small>Telecom closet buildouts</small></li>
      <li><svg class="tick"><use href="#tk"/></svg>Racking<small>Server &amp; network rack install</small></li>
      <li><svg class="tick"><use href="#tk"/></svg>Certifications<small>Verilink LX-8000 testing &amp; reports</small></li>
      <li><svg class="tick"><use href="#tk"/></svg>Low-Voltage Permits<small>Pulled &amp; managed for you</small></li>
    </ul>
  </div>
</div></section>

<section class="serve"><div class="wrap center">
  <div class="eyebrow c">Who we serve</div>
  <h2>Three environments. One trusted cabling partner.</h2>
  <div class="serve-grid" style="text-align:left">
    <div class="seg"><div class="ico"><svg viewBox="0 0 24 24"><path d="M4 11l8-7 8 7v9H4z"/></svg></div><h4>Residential</h4><p>Smart-home cabling and whole-home Wi-Fi for all your devices, entertainment and security systems.</p><ul><li><svg class="tick"><use href="#tk"/></svg>Whole-home Wi-Fi &amp; mesh</li><li><svg class="tick"><use href="#tk"/></svg>Smart-home &amp; AV wiring</li><li><svg class="tick"><use href="#tk"/></svg>Cameras &amp; door access</li></ul></div>
    <div class="seg pop"><span class="tag">MOST REQUESTED</span><div class="ico"><svg viewBox="0 0 24 24"><rect x="5" y="3" width="14" height="18"/><path d="M9 7h2M13 7h2M9 11h2M13 11h2M9 15h2M13 15h2"/></svg></div><h4>Commercial</h4><p>Complete office low-voltage cabling, Wi-Fi, surveillance and access control for your network and security systems.</p><ul><li><svg class="tick"><use href="#tk"/></svg>Structured copper &amp; fiber</li><li><svg class="tick"><use href="#tk"/></svg>Cameras, access &amp; POS</li><li><svg class="tick"><use href="#tk"/></svg>Conference room AV</li></ul></div>
    <div class="seg"><div class="ico"><svg viewBox="0 0 24 24"><path d="M3 21V10l6 4V10l6 4V4h6v17z"/></svg></div><h4>Industrial</h4><p>Structured cabling, IDF and MDF buildouts for warehouses, manufacturing facilities, data centers and more.</p><ul><li><svg class="tick"><use href="#tk"/></svg>IDF / MDF &amp; racking</li><li><svg class="tick"><use href="#tk"/></svg>Warehouse &amp; plant runs</li><li><svg class="tick"><use href="#tk"/></svg>Conduit &amp; fiber backbone</li></ul></div>
  </div>
</div></section>

<section class="why"><div class="wrap why-row">
  <div class="why-photo" role="img" aria-label="Technician terminating bundles of orange and blue network cables, seen from above"><span class="mono">On-site · DMV region</span></div>
  <div class="why-text">
    <div class="eyebrow">Why Wirenexa</div>
    <h2>A full-service partner,<br>not just an installer.</h2>
    <div class="why-list">
      <div class="why-item"><div class="ico"><svg viewBox="0 0 12 12"><use href="#tk"/></svg></div><div><b>30 years, every size of job</b><p>From a single office to a multi-building campus or industrial warehouse — no project is too big or too small.</p></div></div>
      <div class="why-item"><div class="ico"><svg viewBox="0 0 12 12"><use href="#tk"/></svg></div><div><b>Certified &amp; tested workmanship</b><p>Every run is Verilink LX-8000 certified and documented, so you have proof of performance — not just a promise.</p></div></div>
      <div class="why-item"><div class="ico"><svg viewBox="0 0 12 12"><use href="#tk"/></svg></div><div><b>We work with your IT team</b><p>We coordinate directly with your staff and stay until everything is up, tested and running after installation.</p></div></div>
      <div class="why-item"><div class="ico"><svg viewBox="0 0 12 12"><use href="#tk"/></svg></div><div><b>Honest, local &amp; responsive</b><p>A local DMV team that answers the phone, shows up on schedule and gives you a quote within the hour.</p></div></div>
    </div>
  </div>
</div></section>

<section class="stats"><div class="wrap"><div class="stat-row">
  <div class="stat"><b>30</b><i></i><span class="mono">Years in business</span></div>
  <div class="stat"><b>2,500</b><i></i><span class="mono">Projects completed</span></div>
  <div class="stat"><b>4.9</b><i></i><span class="mono">Reviewhub rating</span></div>
  <div class="stat"><b>3</b><i></i><span class="mono">States served · VA·DC·MD</span></div>
</div></div></section>

<section class="process"><div class="wrap center">
  <div class="eyebrow c">How we work</div>
  <h2>A clean, predictable install — start to finish.</h2>
  <div class="steps" style="text-align:left">
    <div class="step"><span class="k">01 / Assess</span><h4>Site Walk &amp; Design</h4><p>We survey the facility, map your needs and engineer a cabling and systems plan built to code and to scale.</p></div>
    <div class="step"><span class="k">02 / Quote</span><h4>Clear Proposal</h4><p>A detailed, transparent quote within the hour — scope, materials and timeline with no surprises.</p></div>
    <div class="step"><span class="k">03 / Install</span><h4>Clean Installation</h4><p>Tidy, labeled, code-compliant runs installed with minimal disruption to your daily operations.</p></div>
    <div class="step"><span class="k">04 / Certify</span><h4>Test &amp; Hand-off</h4><p>Verilink certification, full documentation and a walkthrough with your IT team before we close out.</p></div>
  </div>
</div></section>

<section class="reviews"><div class="wrap center">
  <div class="eyebrow c">Client reviews</div>
  <h2>Commercial clients keep calling us back.</h2>
  <div class="rev-grid" style="text-align:left">
    <div class="rev"><div class="stars">★★★★★</div><p>“Wirenexa ran our entire office network and camera system. Clean work, fully labeled, and certified. They coordinated with our IT vendor without a single hiccup.”</p><div class="who"><i>P</i><div><b>Priya K.</b><span class="mono">Operations Director · Tysons, VA</span></div></div></div>
    <div class="rev"><div class="stars">★★★★★</div><p>“We needed a warehouse re-cabled fast during a move. They scoped it same-day, quoted within an hour, and finished ahead of schedule. Total pros.”</p><div class="who"><i>O</i><div><b>Owen B.</b><span class="mono">Facilities Manager · Beltsville, MD</span></div></div></div>
    <div class="rev"><div class="stars">★★★★★</div><p>“Installed our cameras, access control and conference room AV in one coordinated project. Everything just works, and the documentation was excellent.”</p><div class="who"><i>L</i><div><b>Lena M.</b><span class="mono">IT Manager · Washington, DC</span></div></div></div>
  </div>
  <div class="rated mono">Rated <b style="color:var(--ink)">4.9 / 5</b> across Reviewhub reviews</div>
</div></section>

<section class="contact"><div class="wrap contact-row">
  <div class="contact-left">
    <div class="eyebrow">Get started</div>
    <h2>Let's scope<br>your project.</h2>
    <p class="sub">Tell us about your facility and what you need wired, secured or connected. We'll get back to you with a quote within the hour.</p>
    <div class="cinfo">
      <div class="crow"><div class="ico"><svg viewBox="0 0 24 24"><path d="M5 3h4l2 5-3 2a12 12 0 0 0 6 6l2-3 5 2v4a2 2 0 0 1-2 2A18 18 0 0 1 3 5a2 2 0 0 1 2-2z"/></svg></div><div><span class="mono">Call us</span><b>(888) 555-0142</b><small>Local: 703-555-0190</small></div></div>
      <div class="crow"><div class="ico"><svg viewBox="0 0 24 24"><rect x="3" y="5" width="18" height="14"/><path d="M3 6l9 7 9-7"/></svg></div><div><span class="mono">Email</span><b>sales@wirenexa.com</b></div></div>
      <div class="crow"><div class="ico"><svg viewBox="0 0 24 24"><path d="M12 22s7-7 7-12a7 7 0 0 0-14 0c0 5 7 12 7 12z"/><circle cx="12" cy="10" r="2.5"/></svg></div><div><span class="mono">Office</span><b>1420 Harbor Point Dr, Suite 250</b><small>Reston, VA 20190 · Serving VA · DC · MD</small></div></div>
    </div>
  </div>
  <div class="form">
    <div class="eyebrow">Request a quote</div>
    <h4>Get a response within the hour.</h4>
    <div class="frow"><div class="field"><label>Name *</label><div class="in">Jane Smith</div></div><div class="field"><label>Company</label><div class="in">Acme Inc.</div></div></div>
    <div class="frow"><div class="field"><label>Email *</label><div class="in">jane@company.com</div></div><div class="field"><label>Phone</label><div class="in">(555) 555-5555</div></div></div>
    <div class="field" style="margin-bottom:12px"><label>Service Needed</label><div class="in sel">Structured Cabling (Copper)<span>⌄</span></div></div>
    <div class="field"><label>Project Details *</label><div class="in ta">Tell us about your facility, square footage, timeline, and what you need installed.</div></div>
    <span class="btn btn-red">Request Call Back →</span>
    <div class="note mono">No spam. We only use your info to scope your project.</div>
  </div>
</div></section>

<footer class="footer"><div class="wrap">
  <div class="fcols">
    <div><div class="logo"><i></i>Wirenexa</div><p>A local group of IT professionals delivering fast, reliable and honest low-voltage cabling and systems for commercial and industrial clients across Virginia, Washington DC and Maryland.</p></div>
    <div><span class="mono">Services</span><ul><li>Structured Cabling</li><li>Fiber Optic</li><li>Video Surveillance</li><li>Access Control</li><li>Wireless / WAP</li></ul></div>
    <div><span class="mono">Company</span><ul><li>Why Wirenexa</li><li>Our Process</li><li>Reviews</li><li>Contact</li></ul></div>
    <div><span class="mono">Contact</span><ul><li>(888) 555-0142</li><li>sales@wirenexa.com</li><li>1420 Harbor Point Dr, Ste 250<br>Reston, VA 20190</li></ul></div>
  </div>
  <div class="fbottom"><span class="mono">© 2025 Wirenexa · Licensed &amp; Insured</span><span class="mono">Serving VA · DC · MD</span></div>
</div></footer>
</body>
</html>
```